Maple Lodging Hub website, brand new company, that rents rooms out in houses to milleniuls

We have a site right now that is weak as heck! We could use some punching it up. So we want it to be fun and cool, with added items in for social media (just twitter now) and anything else you want to throw at us. We do have a “blog” in there dedicated to events (we throw a lot of them) so want to incorporate that. Also have an existing design for a hand out that we want to use as our launching pad for colors… you can deviate from it a bit though.

Target Market(s)

25-40 year olds transitioning to the city from other places in the country. Millennial are the min group

Industry/Entity Type

Real Estate

Coding

Coded - Design and coding required

Number of Pages Required

5+ page

Font styles to use
Sans Serif

Requirements
Must have
• Fun look, same pages as those uploaded, but not necessarily the look and feel of what we have already.
• Follow the content of our posted site www.MapleLodgingHub.example
• FOOTER
• LOGO | SITEMAP | SOCIAL LINKS | MAIN CTA REMINDER | CONTACT INFO | COPYRIGHT INFO | TERMS AND CONDITIONS
Nice to have
• Use as many of my graphics as loaded, but feel free to use stock photos as well interlaced. Including both people in their 20’s, 30’s, 40’s, having a fun time or of nice houses, inside and out.

```html
<!DOCTYPE html>
<html lang="en">
<head>
<meta charset="utf-8">
<title>Maple Lodging Hub</title>
<link href="https://fonts.googleapis.com/css2?family=Montserrat:wght@400;500;600;700&display=swap" rel="stylesheet">
<style>
:root{
  --blue:#2a8ee6;
  --green:#2ad12f;
  --ink:#2b2b2b;
  --muted:#444;
  --panel:#f1f1f1;
  --footer:#353535;
  --social:#4a4a4a;
  --footer-text:#cfcfcf;
  --white:#fff;
}
*{box-sizing:border-box;margin:0;padding:0}
html,body{width:759px;height:1200px;overflow:hidden;background:var(--white);font-family:'Montserrat',Arial,sans-serif;color:var(--ink)}
.page{position:relative;width:759px;height:1200px}
.abs{position:absolute}
.hero-photo{left:0;top:0;width:759px;height:337px;background:linear-gradient(180deg,#6f8fb6 0%,#7f9ec4 30%,#5a7aa2 60%,#2f4a35 100%)}
.hero-photo::before{content:"";position:absolute;inset:0;background:radial-gradient(ellipse at 10% 60%,rgba(40,90,40,.75),transparent 35%),radial-gradient(ellipse at 92% 55%,rgba(40,80,40,.75),transparent 35%)}
.topbar{left:0;top:0;width:759px;height:53px;background:rgba(34,40,50,.9)}
.brand{left:148px;top:18px;display:flex;align-items:center;gap:6px;color:#4fa3f0;font-weight:600;font-size:10px;letter-spacing:.3px}
.brand .mark{width:9px;height:9px;background:#4fa3f0}
.nav{right:40px;top:0;display:flex;gap:21px;height:53px;align-items:center}
.nav a{color:var(--white);font-size:7px;font-weight:600;text-decoration:none;position:relative;padding:0 4px}
.nav a.active::after{content:"";position:absolute;left:-6px;right:-6px;top:25px;height:2px;background:var(--blue)}
.hero-title{left:0;width:759px;top:152px;text-align:center;color:var(--white);font-weight:700;font-size:19px;text-shadow:0 1px 3px rgba(0,0,0,.5)}
.hero-sub{left:0;width:759px;top:178px;text-align:center;color:var(--white);font-weight:500;font-size:13px;text-shadow:0 1px 3px rgba(0,0,0,.5)}
.quick{top:215px;width:60px;text-align:center;color:var(--white);font-size:7px;font-weight:600}
.quick svg{display:block;margin:0 auto 3px}
.form-card{left:71px;top:282px;width:612px;height:70px;background:var(--white);box-shadow:0 0 4px rgba(0,0,0,.12)}
.field{top:19px;height:18px;border:1px solid #cfcfcf;font-size:6.5px;color:#777;padding:5px 6px;background:var(--white)}
.submit{left:466px;top:19px;width:125px;height:18px;background:var(--blue);color:var(--white);font-size:7px;font-weight:600;text-align:center;line-height:18px}
.tagline{left:0;width:612px;top:47px;text-align:center;font-size:9px;font-weight:500}
.h2{left:0;width:759px;text-align:center;font-weight:600;font-size:12px}
.lede{left:152px;width:455px;top:390px;text-align:center;font-size:6.4px;line-height:9.6px;color:var(--muted)}
.features{left:0;top:455px;width:759px;height:166px;background:var(--panel)}
.feature{top:10px;width:140px;text-align:center}
.feature h3{font-size:8.5px;font-weight:600;margin:6px 0 6px}
.feature p{font-size:6.4px;line-height:9.6px;color:var(--muted)}
.btn{display:inline-block;background:var(--blue);color:var(--white);font-size:7px;font-weight:600;text-align:center;width:77px;height:19px;line-height:19px}
.btn.green{background:var(--green)}
.feature .btn{position:absolute;top:115px;left:31px}
.band{left:0;top:621px;width:759px;height:213px;background:linear-gradient(100deg,#f3c98a 0%,#fbe8c6 30%,#d9b79a 55%,#8d5c48 75%,#c9b6a8 100%)}
.about{left:151px;top:645px;width:453px;height:181px;background:rgba(255,255,255,.72);text-align:center;padding:14px 12px 0}
.about h3{font-size:8.5px;font-weight:600}
.about .kicker{font-size:6.4px;margin:6px 0 7px}
.about p{font-size:6.4px;line-height:9.6px;color:#333}
.about .btn{margin-top:5px;width:65px;height:18px;line-height:18px;font-size:6.5px}
.card{top:868px;width:214px;height:214px;background:var(--white);box-shadow:0 0 4px rgba(0,0,0,.12);padding:5px}
.card .photo{width:204px}
.card h4{font-size:8.5px;font-weight:600;margin:7px 0 8px}
.card .spec,.card .area{font-size:6.2px;color:#333}
.card .area{margin-top:8px}
.card .btn{position:absolute;right:6px;bottom:10px;width:60px;height:18px;line-height:18px;font-size:6.5px}
.dots{left:369px;top:1090px;display:flex;gap:4px}
.dots span{width:5px;height:5px;border-radius:50%;background:#ddd}
.footer{left:0;top:1102px;width:759px;height:98px;background:var(--footer);color:var(--footer-text)}
.footer-brand{left:40px;top:10px;display:flex;align-items:center;gap:5px;color:var(--white);font-size:8px;font-weight:600}
.footer-brand .mark{width:7px;height:7px;background:var(--blue)}
.sitemap{left:0;width:759px;top:11px;display:flex;justify-content:center;gap:12px;font-size:6.2px;font-weight:500}
.contact{right:40px;top:11px;font-size:6.2px;text-align:right}
.social{top:28px;width:130px;height:22px;background:var(--social);display:flex;align-items:center;justify-content:center}
.social.primary{background:var(--blue)}
.cta{left:0;width:759px;top:57px;display:flex;justify-content:center;align-items:center;gap:8px;font-size:6.8px;font-weight:600;color:var(--white)}
.cta .btn{width:70px;height:14px;line-height:14px;font-size:6.2px}
.legal{left:0;width:759px;top:82px;display:flex;justify-content:center;gap:14px;font-size:6.2px;font-weight:600;color:var(--white)}
.legal span+span{color:var(--footer-text);font-weight:500}
</style>
</head>
<body>
<div class="page">
  <div class="abs hero-photo" role="img" aria-label="Photo of a blue two-storey house with white trim framed by green trees"></div>
  <header class="abs topbar">
    <div class="abs brand"><span class="mark"></span>Maple Lodging Hub</div>
    <nav class="abs nav">
      <a class="active">Welcome</a><a>Our Communities</a><a>Amenities</a><a>Fitting</a><a>Events</a><a>About Us</a><a>Contact</a>
    </nav>
  </header>

  <h1 class="abs hero-title">Welcome</h1>
  <p class="abs hero-sub">Find your perfect rental room today!</p>

  <div class="abs quick" style="left:220px">
    <svg width="32" height="30" viewBox="0 0 32 30" fill="none" stroke="#fff" stroke-width="1.5"><rect x="2" y="6" width="28" height="22"/><line x1="4" y1="3" x2="28" y2="3"/><path d="M4 25l8-9 6 6 4-3 6 6"/><circle cx="22" cy="12" r="3"/></svg>Gallery</div>
  <div class="abs quick" style="left:347px">
    <svg width="36" height="30" viewBox="0 0 36 30" fill="none" stroke="#fff" stroke-width="1.5"><path d="M3 14L14 4l11 10"/><path d="M6 12v16h16V18"/><rect x="12" y="20" width="5" height="8"/><circle cx="27" cy="12" r="5"/><line x1="24" y1="16" x2="20" y2="21"/></svg>Rooms</div>
  <div class="abs quick" style="left:475px">
    <svg width="32" height="30" viewBox="0 0 32 30" fill="none" stroke="#fff" stroke-width="1.5"><rect x="5" y="3" width="22" height="17"/><path d="M2 24h28v3H2z"/><path d="M11 11a7 7 0 0 1 10 0M13 14a4 4 0 0 1 6 0"/><circle cx="16" cy="16.5" r="1" fill="#fff"/></svg>Amenities</div>

  <form class="abs form-card">
    <div class="abs field" style="left:15px;width:139px">Enter your name</div>
    <div class="abs field" style="left:163px;width:139px">Enter your email address</div>
    <div class="abs field" style="left:311px;width:139px">I'm looking for...<span style="float:right">▾</span></div>
    <div class="abs submit">Submit</div>
    <p class="abs tagline">Professional built Communities</p>
  </form>

  <h2 class="abs h2" style="top:370px">Experience the difference</h2>
  <p class="abs lede">Traditional apartments and housing rentals are a thing of the past. We have created an all-encompassing living experience that aligns perfectly with your trendy, yet sophisticated lifestyle. Maple Lodging Hub is unlike anything you have ever experienced before. We invite you to explore our selection of home communities and discover the passion we have for providing wonderful experiences.</p>

  <section class="abs features">
    <div class="abs feature" style="left:153px">
      <svg width="44" height="30" viewBox="0 0 44 30" fill="none" stroke="#5bbf3a" stroke-width="1.5"><path d="M2 14L14 3l12 11"/><path d="M5 12v16h18V15"/><rect x="11" y="19" width="6" height="9"/><path d="M32 26l-8-8a4 4 0 0 1 8-5 4 4 0 0 1 8 5z"/></svg>
      <h3>@Home with MLH</h3>
      <p>After an exhausting day in the office, the thought of hanging out with co workers is the last thing on your mind. But who says you have to conquer a crowded pub...</p>
      <span class="btn">Read More</span>
    </div>
    <div class="abs feature" style="left:307px">
      <svg width="30" height="30" viewBox="0 0 30 30" fill="none" stroke="#27b39a" stroke-width="1.5"><path d="M2 2h26v20H18l-4 6-4-6H2z"/><path d="M8 13l7-6 7 6M10 11v7h10v-7"/></svg>
      <h3>Most Recent Events</h3>
      <p>MLH hosts a number of regular events as well as occasional get togethers. All in efforts of bringing each one of our microcommunities together...</p>
      <span class="btn">Read More</span>
    </div>
    <div class="abs feature" style="left:461px">
      <svg width="36" height="28" viewBox="0 0 36 28" fill="none" stroke="#2a8ee6" stroke-width="1.5"><path d="M2 13L13 3l11 10"/><path d="M5 11v15h16V14"/><rect x="10" y="18" width="5" height="8"/><circle cx="27" cy="12" r="6"/><path d="M27 8v8M23 12h8"/></svg>
      <h3 style="margin-top:3px">Our Latest Addition</h3>
      <p>We are constantly searching for a uniquely beautiful space to create a new community. Check out our latest addition to the family with it's custom finishes and artisan design...</p>
      <span class="btn green">Read More</span>
    </div>
  </section>

  <div class="abs band" role="img" aria-label="Sunlit photo of young friends laughing together outdoors"></div>
  <article class="abs about">
    <h3>It's All About The Community</h3>
    <p class="kicker">Saving money is just a nice perk</p>
    <p>When our founder moved to Riverton it was a major transition period in his life– right in the middle of a slew of major life changes. He picked up a new job, went to a new city, starting over with friends, and trying to start a new life. One of the first things he did– bought a big house. Yea, big mistake. He was house rich, but community poor. Feeling somewhat isolated, he naturally started looking for like-kind people to share his home with. One room at a time, he filled each room in the house with people in similar life transitions–professionals in transition, with similar schedules and a comparable outlook on life. I didn't realize I was doing it at the time, but I turned my "big "mistake into something truly powerful. Many of my tenants have now become some of my best friends. More importantly, they've shown us here at Maple Lodging Hub how much you can flourish in the context of the right community. In the end, it doesn't matter what the little society is built around – church, working out, philanthropy, sports, the arts, or even a common home. You won't find another community like this anywhere.</p>
    <span class="btn">Wanna join Us?</span>
  </article>

  <h2 class="abs h2" style="top:848px">Our Communities</h2>

  <div class="abs card" style="left:34px">
    <div class="photo" role="img" aria-label="Photo of a blue house with a flower garden under a bright sky" style="height:127px;background:linear-gradient(180deg,#4f86cf 0%,#8fb4e2 35%,#6d8bb0 60%,#3f6a36 100%)"></div>
    <h4>Birchwood Place</h4>
    <p class="spec">5 Bedroom | 4.5 Bath | 2,890 Sq. Ft</p>
    <p class="area">East Hollow</p>
    <span class="btn">$500 | Rent</span>
  </div>
  <div class="abs card" style="left:270px">
    <div class="photo" role="img" aria-label="Photo of a cream two-storey house with shrubs and a lawn" style="height:150px;background:linear-gradient(180deg,#9cc0e6 0%,#e9e4d4 35%,#cfc7b0 65%,#4f7a3c 100%)"></div>
    <h4>Alderbrook Park</h4>
    <p class="spec">6 Bedroom | 4 Bath | 2,690 Sq. Ft</p>
    <p class="area">Westmere</p>
    <span class="btn">$500 | Rent</span>
  </div>
  <div class="abs card" style="left:506px">
    <div class="photo" role="img" aria-label="Photo of a backyard patio with chairs and a stone fireplace among trees" style="height:133px;background:linear-gradient(160deg,#8a7a52 0%,#5f6e3a 40%,#3f4d2a 70%,#6b5a44 100%)"></div>
    <h4>Quillan Lane</h4>
    <p class="spec">7 Bedroom | 5 Bath | 3,890 Sq. Ft</p>
    <p class="area">Cedarvale</p>
    <span class="btn">$500 | Rent</span>
  </div>

  <div class="abs dots"><span></span><span></span></div>

  <footer class="abs footer">
    <div class="abs footer-brand"><span class="mark"></span>Maple Lodging Hub</div>
    <nav class="abs sitemap">
      <span>Welcome</span><span>Communities</span><span>Amenities</span><span>Fitting</span><span>Events</span><span>About Us</span><span>Contact</span>
    </nav>
    <div class="abs contact">hello@maplelodginghub.example · (555) 014-2290</div>

    <a class="abs social" style="left:158px" aria-label="Social page">
      <svg width="10" height="10" viewBox="0 0 10 10"><circle cx="5" cy="5" r="4" fill="none" stroke="#fff" stroke-width="1.2"/></svg></a>
    <a class="abs social primary" style="left:312px" aria-label="Updates feed">
      <svg width="10" height="10" viewBox="0 0 10 10"><path d="M1 2h8v5H4l-2 2V7H1z" fill="#fff"/></svg></a>
    <a class="abs social" style="left:466px" aria-label="Photo feed">
      <svg width="10" height="10" viewBox="0 0 10 10" fill="none" stroke="#fff" stroke-width="1.2"><rect x="1" y="2" width="8" height="7"/><circle cx="5" cy="5.5" r="1.6"/></svg></a>

    <div class="abs cta">Ready to move in? Find your perfect rental room today! <span class="btn">Join Us</span></div>
    <p class="abs legal"><span>Copyright © Maple Lodging Hub</span><span>Terms &amp; Conditions</span><span>Privacy</span></p>
  </footer>
</div>
</body>
</html>
```